Marlow Crest Group (Real Estate and Investment)

A high end, clean design.
We are a real estate company with sales, asset management and investment divisions. We want to use a black and white scheme which is really high end feel. The back of the card can just be the logo (black background with the white writing) as we will probably emboss this when we print)

Target Market(s)

High level investors, high end houses for sale

Industry/Entity Type

Business

Contact Information for Business Card

Name, position, phone number and email address
Glen Varley, Managing Director, 0437259064 and glen@marlowcrest-example.com.au

Requirements
Must have
• Back of the card to be the black background with the white writing (as per the attached images). Would like the capacity to emboss the writing and logo

```html
<!DOCTYPE html>
<html lang="en">
<head>
<meta charset="utf-8">
<title>Marlow Crest Group – Business Card</title>
<link rel="stylesheet" href="https://fonts.googleapis.com/css2?family=Lato:wght@300;400;700&display=swap">
<style>
  :root {
    --page-bg: #2b2b2b;
    --card-dark: #1c1c1c;
    --card-light: #3a3a3a;
    --ink: #ffffff;
    --ink-soft: #d9d9d9;
  }
  * { margin: 0; padding: 0; box-sizing: border-box; }
  html, body {
    width: 1200px;
    height: 1166px;
    overflow: hidden;
  }
  body {
    background: var(--page-bg);
    font-family: "Lato", Arial, sans-serif;
    color: var(--ink);
    position: relative;
  }
  .card {
    position: absolute;
    left: 160px;
    width: 880px;
    height: 503px;
    background: linear-gradient(115deg, var(--card-dark) 0%, var(--card-light) 48%, var(--card-dark) 100%);
    box-shadow: 0 18px 40px rgba(0, 0, 0, 0.55);
  }
  .card--back { top: 53px; }
  .card--front { top: 609px; }

  /* Brand lockup */
  .brand {
    display: flex;
    align-items: center;
    gap: 22px;
  }
  .brand__dot {
    width: 34px;
    height: 34px;
    border: 2px solid var(--ink);
    border-radius: 50%;
    flex: none;
  }
  .brand__name {
    font-weight: 300;
    text-transform: uppercase;
    letter-spacing: 0.12em;
    color: var(--ink);
    white-space: nowrap;
  }
  .card--back .brand {
    position: absolute;
    left: 50%;
    top: 50%;
    transform: translate(-50%, -50%);
  }
  .card--back .brand__name { font-size: 44px; }

  /* Front: stacked brand left, divider, contact right */
  .card--front .brand {
    position: absolute;
    left: 70px;
    top: 250px;
    flex-direction: column;
    align-items: flex-start;
    gap: 18px;
  }
  .card--front .brand__dot { width: 40px; height: 40px; }
  .card--front .brand__name {
    font-size: 26px;
    letter-spacing: 0.06em;
  }

  .divider {
    position: absolute;
    left: 455px;
    top: 150px;
    width: 1px;
    height: 170px;
    background: var(--ink);
  }
  .contact {
    position: absolute;
    left: 495px;
    top: 150px;
  }
  .contact__name {
    font-size: 30px;
    font-weight: 700;
    line-height: 1.1;
  }
  .contact__role {
    font-size: 21px;
    font-weight: 300;
    color: var(--ink-soft);
    margin-top: 4px;
  }
  .contact__list {
    list-style: none;
    margin-top: 18px;
  }
  .contact__item {
    display: flex;
    align-items: center;
    gap: 12px;
    font-size: 21px;
    font-weight: 300;
    line-height: 1.45;
  }
  .contact__icon {
    width: 16px;
    height: 16px;
    flex: none;
    fill: var(--ink);
  }
</style>
</head>
<body>
  <section class="card card--back" aria-label="Card back">
    <div class="brand">
      <span class="brand__dot" aria-hidden="true"></span>
      <span class="brand__name">Marlow Crest Group</span>
    </div>
  </section>

  <section class="card card--front" aria-label="Card front">
    <div class="brand">
      <span class="brand__dot" aria-hidden="true"></span>
      <span class="brand__name">Marlow Crest Group</span>
    </div>

    <div class="divider" aria-hidden="true"></div>

    <div class="contact">
      <p class="contact__name">Glen Varley</p>
      <p class="contact__role">Managing Director</p>
      <ul class="contact__list">
        <li class="contact__item">
          <svg class="contact__icon" viewBox="0 0 16 16" aria-hidden="true">
            <path d="M3.6 1.2c.5-.3 1.1-.2 1.4.3l1.4 2.2c.3.5.2 1.1-.2 1.4l-1 .8c.7 1.6 1.9 2.9 3.5 3.7l.8-1c.4-.4 1-.5 1.4-.2l2.2 1.4c.5.3.6.9.3 1.4l-.8 1.3c-.5.8-1.5 1.1-2.4.8C6.1 12.1 3.4 9.3 2.2 5.3c-.3-.9 0-1.9.8-2.4z"/>
          </svg>
          <span>0437 259 064</span>
        </li>
        <li class="contact__item">
          <svg class="contact__icon" viewBox="0 0 16 16" aria-hidden="true">
            <path d="M1 3.5h14v1L8 9 1 4.5z"/>
            <path d="M1 6l7 4.5L15 6v6.5H1z"/>
          </svg>
          <span>glen@marlowcrest-example.com.au</span>
        </li>
      </ul>
    </div>
  </section>
</body>
</html>
```